Business Card Design and Stationary design for consulting firm

Harbourline Sourcing are looking for a new business card design and a design for their A4 letterhead / A4 invoices.

We are seeking to heavily increase our brand awareness and require a business card that's professional in appearance but also shows flare and innovation. A card design that people will remember.

About Us
Harbourline Sourcing are `The Sourcing Crew’.
Our mission is to be one of Australia’s greatest companies. Our aim is to help our customers achieve the best result from their purchasing experience.

Our Requirement:
• IMPACT! IMPACT! IMPACT!
• BUSINESS & PROFESSIONAL LOOKING

• Our business colours are orange, blue and green (See the logo attached).

We have provided an Art Design specification (attached) that needs to be followed for you to win the design. This also has the font, which is used on the logo.

We are after a two sided business card

Side One should have the:
The company Logo
The Sourcing Crew
www.harbourlinesourcing.com.au
Procure | Personnel | Probity & Privacy
Sydney | Melbourne | Adelaide | Brisbane

Side Two
Logo (optional)
Harbourline Sourcing (optional)
Employee details (details listed below)

The above format is our preferred option, but if you think you can come up with something better, feel free to put it forward.

We are leaving the design up to you, but it must incorporate the logo.

We will need a template that we can change the employee details on, as we will be adding more staff over the coming months.

The details below are for one employee per card with the same design.
------------------------

Employee Details:

Marcus Del Arroyo MBA, MMgmtStratProc
Principal Consultant
0491 372 618
Marcus@harbourlinesourcing.com.au

Brianna Tolley
Consulting Manager
0462 915 308
Brianna@harbourlinesourcing.com.au

Our website is www.harbourlinesourcing.com.au

The Letterhead / invoice needs to incorporate:
the company Logo
The Sourcing Crew
Sydney | Melbourne | Adelaide | Brisbane but otherwise the design is over to you.

This file needs to be delivered in word format as other detail will be added to the documents.

We look forward to you award winning designs. If you require any further information please feel free to contact us.

Regards
Harbourline Sourcing

Target Market(s)

Our Target market is companies with 80+ employees. The market we segment is heavily male based, between the ages of 35-55 years of age.

Industry/Entity Type

Consulting

Contact Information for Business Card

See Project Description

Font styles to use
Other font styles liked:
• See Art Specification

Requirements
Must have
• Company Colours, See Project Description
Should not have
• Be outside the Art specification guidelines

```html
<!DOCTYPE html>
<html lang="en">
<head>
<meta charset="utf-8">
<title>Harbourline Sourcing – Business Card</title>
<link rel="stylesheet" href="https://fonts.googleapis.com/css2?family=Roboto:wght@300;400;500&display=swap">
<style>
  :root {
    --page-bg: #e9ecef;
    --card-white: #f7f7f7;
    --brand-blue: #1a9fd6;
    --brand-blue-light: #3cc0e8;
    --brand-blue-deep: #0f7fb8;
    --swoosh-grey: #c9c9c9;
    --ink-dark: #333b42;
    --ink-grey: #4a4a4a;
    --text-white: #ffffff;
  }
  * { box-sizing: border-box; margin: 0; padding: 0; }
  html, body { width: 1200px; height: 780px; overflow: hidden; }
  body {
    background: var(--page-bg);
    font-family: "Roboto", Arial, sans-serif;
    position: relative;
  }
  .card {
    position: absolute;
    top: 225px;
    width: 540px;
    height: 330px;
    border-radius: 16px;
    overflow: hidden;
    box-shadow: 0 6px 18px rgba(0,0,0,0.18);
  }

  /* ---------- Staff side ---------- */
  .card--staff { left: 40px; background: var(--card-white); }
  .card--staff .wave { position: absolute; inset: 0; width: 100%; height: 100%; }

  .brand {
    position: absolute;
    display: flex;
    align-items: center;
    gap: 10px;
  }
  .brand__dot {
    width: 22px; height: 22px; border-radius: 50%;
    flex: none;
  }
  .brand__name {
    font-weight: 500;
    letter-spacing: 0.06em;
    line-height: 1.1;
    text-transform: uppercase;
  }
  .card--staff .brand { left: 30px; top: 228px; }
  .card--staff .brand__dot { background: var(--brand-blue); }
  .card--staff .brand__name { color: var(--ink-dark); font-size: 20px; }

  .staff {
    position: absolute;
    right: 34px;
    top: 24px;
    text-align: right;
  }
  .staff__name { color: var(--brand-blue); font-size: 22px; font-weight: 500; line-height: 1.2; }
  .staff__role { color: var(--ink-grey); font-size: 14px; font-weight: 400; margin-top: 2px; }

  .contact-icons {
    position: absolute;
    right: 34px;
    top: 128px;
    display: flex;
    gap: 6px;
  }
  .contact-icons svg {
    width: 20px; height: 20px;
    border: 1.5px solid var(--text-white);
    border-radius: 4px;
    padding: 2px;
  }
  .contact {
    position: absolute;
    right: 34px;
    top: 162px;
    list-style: none;
    text-align: right;
    color: var(--text-white);
    font-size: 12.5px;
    line-height: 1.75;
  }

  /* ---------- Company side ---------- */
  .card--company {
    left: 620px;
    background: radial-gradient(ellipse at 50% 40%, var(--brand-blue-light) 0%, var(--brand-blue) 55%, var(--brand-blue-deep) 100%);
  }
  .card--company .brand {
    left: 0; right: 0; top: 96px;
    justify-content: center;
  }
  .card--company .brand__dot { background: var(--text-white); }
  .card--company .brand__name { color: var(--text-white); font-size: 26px; }
  .card--company .rule {
    position: absolute;
    left: 150px; right: 150px; top: 145px;
    height: 1.5px;
    background: var(--text-white);
  }
  .services {
    position: absolute;
    left: 0; right: 0; top: 164px;
    text-align: center;
    color: var(--text-white);
    font-size: 14px;
    line-height: 1.55;
  }
  .web-strip {
    position: absolute;
    left: 0; right: 0; bottom: 0;
    height: 42px;
    background: var(--card-white);
    display: flex;
    align-items: center;
    padding-left: 28px;
    color: var(--brand-blue-deep);
    font-size: 14px;
    font-weight: 500;
  }
</style>
</head>
<body>

  <section class="card card--staff" aria-label="Business card, staff side">
    <svg class="wave" viewBox="0 0 540 330" preserveAspectRatio="none" aria-hidden="true">
      <path d="M130,330 C205,312 248,272 255,218" fill="none" stroke="var(--swoosh-grey)" stroke-width="10" stroke-linecap="round"/>
      <path d="M540,95 C380,95 300,130 280,200 C268,250 262,300 250,330 L540,330 Z" fill="var(--brand-blue)"/>
      <path d="M540,80 C370,80 285,120 265,195 C252,248 246,300 234,330" fill="none" stroke="var(--brand-blue-light)" stroke-width="5"/>
      <path d="M540,125 C410,125 335,160 315,220 C303,262 298,305 290,330" fill="none" stroke="#ffffff" stroke-opacity="0.45" stroke-width="4"/>
    </svg>

    <div class="brand">
      <span class="brand__dot"></span>
      <span class="brand__name">Harbourline<br>Sourcing</span>
    </div>

    <div class="staff">
      <p class="staff__name">Brianna Tolley</p>
      <p class="staff__role">Consulting Manager</p>
    </div>

    <div class="contact-icons" aria-hidden="true">
      <svg viewBox="0 0 16 16"><rect x="5" y="2" width="6" height="12" rx="1" fill="none" stroke="#fff" stroke-width="1.4"/></svg>
      <svg viewBox="0 0 16 16"><rect x="2" y="4" width="12" height="8" fill="none" stroke="#fff" stroke-width="1.4"/><path d="M2 4 L8 9 L14 4" fill="none" stroke="#fff" stroke-width="1.4"/></svg>
      <svg viewBox="0 0 16 16"><circle cx="8" cy="8" r="6" fill="none" stroke="#fff" stroke-width="1.4"/><path d="M2 8 H14 M8 2 C5 5 5 11 8 14 M8 2 C11 5 11 11 8 14" fill="none" stroke="#fff" stroke-width="1.1"/></svg>
    </div>

    <ul class="contact">
      <li>0462 915 308</li>
      <li>Brianna@harbourlinesourcing.com.au</li>
      <li>www.harbourlinesourcing.com.au</li>
    </ul>
  </section>

  <section class="card card--company" aria-label="Business card, company side">
    <div class="brand">
      <span class="brand__dot"></span>
      <span class="brand__name">Harbourline Sourcing</span>
    </div>
    <div class="rule"></div>
    <p class="services">
      Procure | Personnel | Probity &amp; Privacy | Sydney<br>
      Melbourne | Adelaide | Brisbane
    </p>
    <div class="web-strip">www.harbourlinesourcing.com.au</div>
  </section>

</body>
</html>
```